Varlow Landscaping

Create a website for a new landscaping company. I have a logo already and description of services offered. I have a website that I would like all inquiries and appointments to get forwarded to. I need just need it well organized so that a husband and wife team can manage it easily. This is a company that will continue to grow over time and will need to add more services under new tabs over time. If you need the email where appointments and inquiries should go please send me a message.
Services offered are: Weekly/bi weekly mowing, weed eating and edging, Plant installation pinestraw & mulch installation, weed & feed, leaf removal and yard clean up.

```html
<!DOCTYPE html>
<html lang="en">
<head>
<meta charset="utf-8">
<title>Varlow Landscaping – Lawn Care &amp; Landscaping</title>
<link href="https://fonts.googleapis.com/css2?family=Alegreya:wght@700;800&family=Poppins:ital,wght@0,400;0,500;0,600;0,700;1,400&display=swap" rel="stylesheet">
<style>
:root{
  --green:#3d8b1f;
  --green-dark:#2b6a12;
  --green-deep:#22570c;
  --yellow:#f7bd2a;
  --yellow-soft:#fffbe5;
  --ink:#1f1f1f;
  --muted:#444;
  --line:#e3e3e3;
  --white:#fff;
}
*{box-sizing:border-box;margin:0;padding:0}
html,body{width:1200px;height:5150px;overflow:hidden}
body{position:relative;background:var(--white);font-family:"Poppins",sans-serif;color:var(--ink)}
.abs{position:absolute}
.serif{font-family:"Alegreya",serif;font-weight:800}
.section-title{font-family:"Alegreya",serif;font-weight:800;color:var(--green);font-size:52px;letter-spacing:1px;line-height:1}

/* header */
.topbar{left:688px;top:0;width:512px;height:68px;background:var(--yellow);border-bottom-left-radius:34px;display:flex;align-items:center;gap:40px;padding-left:52px}
.topbar .item{display:flex;align-items:center;gap:10px}
.topbar .ico{width:28px;height:28px;background:var(--green);border-radius:5px;display:flex;align-items:center;justify-content:center}
.topbar .lbl{font-size:13px;font-weight:600;color:var(--green-dark);line-height:1.15}
.topbar .val{font-size:14px;color:var(--ink);line-height:1.2}
.brand{left:68px;top:8px;width:156px;height:194px;background:var(--white);padding:6px;z-index:3;box-shadow:0 2px 6px rgba(0,0,0,.15)}
.brand .mark{width:100%;height:100%;background:var(--green-dark);display:flex;flex-direction:column;align-items:center;justify-content:center;gap:10px}
.brand .dot{width:34px;height:34px;border-radius:50%;background:var(--yellow)}
.brand .name{font-family:"Poppins",sans-serif;font-weight:700;color:var(--white);font-size:17px;text-align:center;line-height:1.2}
.nav{left:496px;top:96px;display:flex;gap:32px;font-size:13.5px;font-weight:500}
.nav a{color:var(--ink);text-decoration:none;padding-bottom:10px}
.nav a.active{color:var(--green);border-bottom:2px solid var(--green)}
.btn-book{left:980px;top:86px;width:154px;height:44px;border-radius:22px;background:var(--green);color:var(--white);font-size:14px;font-weight:700;display:flex;align-items:center;justify-content:center}

/* hero */
.hero{left:0;top:160px;width:1200px;height:800px}
.hero-text{left:0;top:575px;width:1200px;text-align:center;color:var(--white)}
.hero-text .kicker{font-size:42px;line-height:1}
.hero-text .headline{font-size:70px;line-height:1;margin-top:22px;letter-spacing:1px}
.btn-pill{display:flex;align-items:center;justify-content:space-between;border-radius:40px;font-weight:700}
.arrow-dot{border-radius:50%;background:var(--green);display:flex;align-items:center;justify-content:center}
.hero-btn{left:458px;top:740px;width:292px;height:76px;background:var(--white);color:var(--green-dark);font-size:29px;padding:0 8px 0 36px;box-shadow:0 4px 14px rgba(0,0,0,.2)}
.hero-btn .arrow-dot{width:60px;height:60px}

/* diamonds */
.diamond{position:absolute;transform:rotate(45deg);border-radius:90px;overflow:hidden}

/* about */
.about-copy{left:668px;top:1144px;width:462px}
.about-copy .lead{font-size:16px;font-weight:600;line-height:1.65;margin-top:28px;text-align:justify}
.about-copy .body{font-size:13.5px;line-height:2;color:var(--muted);margin-top:22px;text-align:justify}
.outline-btn{border:2px solid var(--green);background:var(--white);color:var(--green-dark);font-size:15px;padding:0 4px 0 24px;height:52px}
.outline-btn .arrow-dot{width:40px;height:40px}

/* services */
.services-intro{left:68px;top:1816px;width:800px;font-size:13.5px;line-height:2;color:var(--muted)}
.circle-btn{width:58px;height:58px;border-radius:50%;display:flex;align-items:center;justify-content:center}
.circle-btn.prev{border:2px solid var(--yellow);background:var(--white)}
.circle-btn.next{background:var(--green)}
.service-card{top:1922px;width:342px;height:364px;border-radius:14px;overflow:hidden}
.service-card .caption{position:absolute;left:0;bottom:20px;width:100%;text-align:center;color:var(--white);font-size:19px;font-weight:600}
.service-card.featured{background:linear-gradient(160deg,#3f9323,#2f7415);color:var(--white);text-align:center;padding:70px 34px 0}
.service-card.featured h3{font-size:19px;font-weight:500;letter-spacing:.5px}
.service-card.featured .rule{width:64px;height:3px;background:var(--white);margin:14px auto 22px}
.service-card.featured p{font-size:14px;line-height:1.9}
.service-card.featured .more{display:inline-block;margin-top:22px;background:var(--yellow);color:var(--green-deep);font-size:12px;font-weight:700;border-radius:18px;padding:8px 24px}

/* testimonials */
.testi-title{left:0;top:2696px;width:1200px;text-align:center}
.testi-card{top:2810px;width:320px;height:254px;background:var(--white);box-shadow:0 4px 18px rgba(0,0,0,.1);padding:34px 26px 0}
.testi-card p{font-style:italic;font-size:13.5px;line-height:1.78;color:var(--muted);text-align:justify}
.testi-card .who{display:flex;align-items:center;gap:14px;margin-top:16px}
.testi-card .avatar{width:64px;height:64px;border-radius:50%;border:4px solid #eee}
.testi-card .name{color:var(--green);font-weight:700;font-size:17px}
.testi-card .stars{color:var(--yellow);font-size:12px;letter-spacing:2px}
.testi-card .quote{position:absolute;right:22px;bottom:16px;font-family:"Alegreya",serif;font-size:90px;color:var(--green);line-height:.5;height:40px}

/* cta */
.cta{left:68px;top:3460px;width:1064px;height:522px;border-radius:70px;overflow:hidden;background:linear-gradient(160deg,#5aa52c,#3f8a1d 50%,#2a6210)}
.cta-text{left:0;top:3590px;width:1200px;text-align:center;color:var(--white);font-size:66px;line-height:1.1;text-shadow:0 3px 8px rgba(0,0,0,.35)}
.cta-btn{left:354px;top:3780px;width:482px;height:76px;background:var(--yellow);color:var(--green-deep);font-size:27px;padding:0 8px 0 38px}
.cta-btn .arrow-dot{width:60px;height:60px}

/* contact */
.field{height:50px;background:var(--white);box-shadow:0 2px 10px rgba(0,0,0,.12);border-radius:4px;display:flex;align-items:center;gap:12px;padding-left:22px;font-size:12.5px;color:#555}
.field.msg{align-items:flex-start;padding-top:18px;height:96px}
.field .caret{margin-left:auto;margin-right:20px;font-size:10px}
.enquire{left:68px;top:4604px;width:228px;height:54px;border:2px solid var(--green);background:var(--white);color:var(--green-dark);font-size:17px;font-weight:600;padding:0 4px 0 24px}
.enquire .arrow-dot{width:42px;height:42px}

/* footer */
.footer{left:0;top:4680px;width:1200px;height:470px}
.f-contact{top:4928px;display:flex;align-items:center;gap:14px;color:var(--white);font-size:13.5px;line-height:1.35}
.f-contact .ico{width:34px;height:34px;background:var(--yellow);border-radius:6px;display:flex;align-items:center;justify-content:center}
.f-rule{left:68px;width:1064px;height:1px;background:rgba(255,255,255,.35)}
.f-links{left:68px;top:5038px;width:1064px;display:flex;justify-content:center;color:var(--white);font-size:13px;font-weight:500}
.f-links span{padding:0 52px;position:relative}
.f-links span+span::before{content:"|";position:absolute;left:-3px}
.copyright{left:68px;top:5120px;color:var(--white);font-size:11.5px}
.socials{left:1016px;top:5116px;display:flex;gap:6px}
.socials span{width:24px;height:24px;background:var(--yellow);border-radius:3px;display:block}
</style>
</head>
<body>

<!-- header -->
<div class="abs topbar">
  <div class="item">
    <div class="ico"><svg width="16" height="16" viewBox="0 0 24 24" fill="#fff"><path d="M6.6 10.8a15 15 0 0 0 6.6 6.6l2.2-2.2c.3-.3.7-.4 1-.2 1.1.4 2.3.6 3.6.6.6 0 1 .4 1 1V20c0 .6-.4 1-1 1A17 17 0 0 1 3 4c0-.6.4-1 1-1h3.5c.6 0 1 .4 1 1 0 1.3.2 2.5.6 3.6.1.3 0 .7-.2 1z"/></svg></div>
    <div><div class="lbl">Call Us</div><div class="val">012 555 0147</div></div>
  </div>
  <div class="item">
    <div class="ico"><svg width="16" height="16" viewBox="0 0 24 24" fill="#fff"><path d="M3 5h18a1 1 0 0 1 1 1v12a1 1 0 0 1-1 1H3a1 1 0 0 1-1-1V6a1 1 0 0 1 1-1zm1 2v.3l8 5.2 8-5.2V7z"/></svg></div>
    <div><div class="lbl">Email Us</div><div class="val">hello@varlowyards.com</div></div>
  </div>
</div>

<div class="abs brand">
  <div class="mark"><span class="dot"></span><span class="name">Varlow<br>Landscaping</span></div>
</div>

<nav class="abs nav">
  <a class="active">HOME</a><a>ABOUT US</a><a>SERVICES</a><a>ENQUIRIES</a><a>CONTACT US</a>
</nav>
<div class="abs btn-book">BOOK NOW</div>

<!-- hero -->
<svg class="abs hero" viewBox="0 0 1200 800" preserveAspectRatio="none">
  <defs>
    <linearGradient id="heroFill" x1="0" y1="0" x2="1" y2="1">
      <stop offset="0" stop-color="#2f5a16"/>
      <stop offset=".45" stop-color="#5a8a2c"/>
      <stop offset=".8" stop-color="#3d6a1e"/>
      <stop offset="1" stop-color="#2a4a12"/>
    </linearGradient>
  </defs>
  <path d="M0 540 L0 640 C200 720 420 800 600 795 C760 790 880 740 1200 560 V500 Z" fill="var(--yellow)"/>
  <path role="img" aria-label="Photo of a gardener trimming a hedge with shears" d="M0 0 H1200 V580 C1000 680 820 760 640 770 C460 778 260 700 0 550 Z" fill="url(#heroFill)"/>
</svg>
<div class="abs hero-text serif">
  <div class="kicker">WELCOME TO VARLOW</div>
  <div class="headline">LAWN CARE &amp; LANDSCAPING</div>
</div>
<div class="abs btn-pill hero-btn">BOOK NOW <span class="arrow-dot"><svg width="26" height="26" viewBox="0 0 24 24" fill="none" stroke="#fff" stroke-width="2.6"><path d="M6 18L18 6M9 6h9v9"/></svg></span></div>

<!-- about -->
<div class="diamond" style="left:150px;top:1140px;width:390px;height:390px;background:var(--yellow)"></div>
<div class="diamond" role="img" aria-label="Photo of a landscaper trimming a hedge in a garden" style="left:164px;top:1120px;width:390px;height:390px;background:linear-gradient(135deg,#8fb56a,#3f6e22 60%,#2c4d18)"></div>

<div class="abs about-copy">
  <h2 class="section-title">ABOUT US</h2>
  <p class="lead">Lorem ipsum dolor sit amet, consectetur adipiscing elit. Aenean semper nunc urna, sit amet lobortis erat scelerisque sit amet.</p>
  <p class="body">Lorem ipsum dolor sit amet, consectetur adipiscing elit, sed do ei usmod tempor incididunt ut labore et dolore magna aliqua. Ut enim ad minim veniam, quis nostrud exercitation ullamco laboris nisi ut aliquip ex ea commodo consequat. Duis aute irure dolor in reprehenderit in voluptate velit esse cillum dolore eu fugiat.</p>
</div>
<div class="abs btn-pill outline-btn" style="left:668px;top:1476px;width:186px">READ MORE <span class="arrow-dot"><svg width="18" height="18" viewBox="0 0 24 24" fill="none" stroke="#fff" stroke-width="2.8"><path d="M6 18L18 6M9 6h9v9"/></svg></span></div>

<!-- services -->
<h2 class="abs section-title" style="left:68px;top:1734px">OUR SERVICES</h2>
<p class="abs services-intro">Lorem ipsum dolor sit amet, consectetur adipiscing elit, sed do eiusmod tempor incididunt ut labore et dolore magna aliqua. Quis ipsum suspendisse ultrices gravida. Risus commodo viverra maecenas accumsan.</p>
<div class="abs circle-btn prev" style="left:1008px;top:1805px"><svg width="18" height="18" viewBox="0 0 24 24" fill="none" stroke="var(--yellow)" stroke-width="3"><path d="M15 5l-7 7 7 7"/></svg></div>
<div class="abs circle-btn next" style="left:1074px;top:1805px"><svg width="18" height="18" viewBox="0 0 24 24" fill="none" stroke="#fff" stroke-width="3"><path d="M9 5l7 7-7 7"/></svg></div>

<div class="abs service-card" role="img" aria-label="Photo of a man mowing a lawn beside a gazebo" style="left:68px;background:linear-gradient(180deg,#6d8a56,#3d6a26 60%,#2d4f1a)">
  <div class="caption">Weekly/bi Weekly Mowing</div>
</div>
<div class="abs service-card featured" style="left:430px">
  <h3>WEED EATING AND EDGING</h3>
  <div class="rule"></div>
  <p>Lorem ipsum dolor sit amet, consecte tur adipiscing elit. Pellentesque erat enim, varius vel libero in, fringilla.</p>
  <span class="more">READ MORE</span>
</div>
<div class="abs service-card" role="img" aria-label="Photo of a rake gathering autumn leaves on grass" style="left:792px;background:linear-gradient(180deg,#8a8a74,#5f7a3a 55%,#3d6a1e)">
  <div class="caption">Leaf Removal &amp; Yard Clean Up</div>
</div>

<div class="abs btn-pill outline-btn" style="left:506px;top:2350px;width:188px;height:52px">VIEW MORE <span class="arrow-dot"><svg width="18" height="18" viewBox="0 0 24 24" fill="none" stroke="#fff" stroke-width="2.8"><path d="M6 18L18 6M9 6h9v9"/></svg></span></div>

<!-- testimonials -->
<svg class="abs" style="left:0;top:2500px" width="1200" height="820" viewBox="0 0 1200 820">
  <path d="M0 70 C300 40 480 0 600 0 C720 0 900 40 1200 70 V620 C900 660 720 820 600 820 C480 820 300 660 0 620 Z" fill="var(--yellow-soft)"/>
</svg>
<h2 class="abs section-title testi-title">OUR TESTIMONIALS</h2>

<div class="abs testi-card" style="left:74px">
  <p>Lorem ipsum dolor sit amet, consecte tur adipiscing elit. Pellentesque aliquet eros vitae placerat hendrerit. Maece nas maximus commodo sapien, vitae lobortis ligula</p>
  <div class="who"><span class="avatar" role="img" aria-label="Customer portrait" style="background:#d9b89a"></span><div><div class="name">Marla Quince</div><div class="stars">★★★★★</div></div></div>
  <div class="quote">”</div>
</div>
<div class="abs testi-card" style="left:440px">
  <p>Lorem ipsum dolor sit amet, consecte tur adipiscing elit. Pellentesque aliquet eros vitae placerat hendrerit. Maece nas maximus commodo sapien, vitae lobortis ligula</p>
  <div class="who"><span class="avatar" role="img" aria-label="Customer portrait" style="background:#6b4a38"></span><div><div class="name">Jonah Pell</div><div class="stars">★★★★★</div></div></div>
  <div class="quote">”</div>
</div>
<div class="abs testi-card" style="left:804px">
  <p>Lorem ipsum dolor sit amet, consecte tur adipiscing elit. Pellentesque aliquet eros vitae placerat hendrerit. Maece nas maximus commodo sapien, vitae lobortis ligula</p>
  <div class="who"><span class="avatar" role="img" aria-label="Customer portrait" style="background:#d9b89a"></span><div><div class="name">Marla Quince</div><div class="stars">★★★★★</div></div></div>
  <div class="quote">”</div>
</div>

<div class="abs circle-btn prev" style="left:550px;top:3124px;width:44px;height:44px"><svg width="14" height="14" viewBox="0 0 24 24" fill="none" stroke="var(--yellow)" stroke-width="3"><path d="M15 5l-7 7 7 7"/></svg></div>
<div class="abs circle-btn next" style="left:604px;top:3124px;width:44px;height:44px"><svg width="14" height="14" viewBox="0 0 24 24" fill="none" stroke="#fff" stroke-width="3"><path d="M9 5l7 7-7 7"/></svg></div>

<!-- call to action -->
<div class="abs cta" role="img" aria-label="Photo of a lawn mower cutting bright green grass"></div>
<div class="abs cta-text serif">Create Beautiful Gardens<br>That Inspire Every Single Day</div>
<div class="abs btn-pill cta-btn">MAKE YOUR APPOINTMENT <span class="arrow-dot"><svg width="26" height="26" viewBox="0 0 24 24" fill="none" stroke="#fff" stroke-width="2.6"><path d="M6 18L18 6M9 6h9v9"/></svg></span></div>

<!-- contact -->
<h2 class="abs section-title" style="left:68px;top:4154px">CONTACT US</h2>
<div class="abs field" style="left:68px;top:4252px;width:292px"><svg width="11" height="11" viewBox="0 0 24 24" fill="#666"><circle cx="12" cy="7" r="5"/><path d="M2 23c0-6 4-9 10-9s10 3 10 9z"/></svg>First Name</div>
<div class="abs field" style="left:370px;top:4252px;width:292px;padding-left:40px"><svg width="13" height="11" viewBox="0 0 24 18" fill="#666"><path d="M0 0h24v18H0zm2 2v1l10 6 10-6V2z"/></svg>E-Mail</div>
<div class="abs field" style="left:68px;top:4322px;width:292px"><svg width="9" height="13" viewBox="0 0 14 22" fill="none" stroke="#666" stroke-width="2"><rect x="1" y="1" width="12" height="20" rx="2"/></svg>Phone Number</div>
<div class="abs field" style="left:370px;top:4322px;width:292px;padding-left:40px"><svg width="10" height="13" viewBox="0 0 20 26" fill="#666"><path d="M10 0a10 10 0 0 1 10 10c0 7-10 16-10 16S0 17 0 10A10 10 0 0 1 10 0zm0 6a4 4 0 1 0 0 8 4 4 0 0 0 0-8z"/></svg>Address</div>
<div class="abs field" style="left:68px;top:4390px;width:594px"><svg width="11" height="11" viewBox="0 0 24 24"><circle cx="12" cy="12" r="10" fill="none" stroke="#888" stroke-width="2"/><circle cx="12" cy="12" r="5" fill="#666"/></svg>Select Service<span class="caret">▼</span></div>
<div class="abs field msg" style="left:68px;top:4460px;width:594px"><svg width="11" height="11" viewBox="0 0 24 24" fill="#666"><circle cx="12" cy="12" r="11"/></svg>Message</div>
<div class="abs btn-pill enquire">ENQUIRE NOW <span class="arrow-dot"><svg width="18" height="18" viewBox="0 0 24 24" fill="none" stroke="#fff" stroke-width="2.8"><path d="M6 18L18 6M9 6h9v9"/></svg></span></div>

<div class="diamond" style="left:778px;top:4236px;width:296px;height:296px;background:var(--yellow);border-radius:70px"></div>
<div class="diamond" role="img" aria-label="Photo of a trowel planting seedlings in soil" style="left:766px;top:4222px;width:296px;height:296px;border-radius:70px;background:linear-gradient(135deg,#bcd39a,#6f8f44 45%,#4a3a28)"></div>

<!-- footer -->
<svg class="abs footer" viewBox="0 0 1200 470" preserveAspectRatio="none">
  <path d="M0 250 C300 220 600 70 900 40 C1050 25 1150 10 1200 0 V470 H0 Z" fill="var(--yellow)"/>
  <path d="M0 230 C320 225 600 120 880 95 C1000 85 1120 75 1200 70 V470 H0 Z" fill="var(--green-dark)"/>
</svg>

<div class="abs f-contact" style="left:228px">
  <div class="ico"><svg width="18" height="18" viewBox="0 0 24 24" fill="#fff"><path d="M6.6 10.8a15 15 0 0 0 6.6 6.6l2.2-2.2c.3-.3.7-.4 1-.2 1.1.4 2.3.6 3.6.6.6 0 1 .4 1 1V20c0 .6-.4 1-1 1A17 17 0 0 1 3 4c0-.6.4-1 1-1h3.5c.6 0 1 .4 1 1 0 1.3.2 2.5.6 3.6.1.3 0 .7-.2 1z"/></svg></div>
  <div>CALL US<br>012 555 0147</div>
</div>
<div class="abs f-contact" style="left:452px">
  <div class="ico"><svg width="18" height="14" viewBox="0 0 24 18" fill="#fff"><path d="M0 0h24v18H0zm2 2v1l10 6 10-6V2z"/></svg></div>
  <div>EMAIL US<br>hello@varlowyards.com</div>
</div>
<div class="abs f-contact" style="left:756px">
  <div class="ico"><svg width="14" height="18" viewBox="0 0 20 26" fill="#fff"><path d="M10 0a10 10 0 0 1 10 10c0 7-10 16-10 16S0 17 0 10A10 10 0 0 1 10 0zm0 6a4 4 0 1 0 0 8 4 4 0 0 0 0-8z"/></svg></div>
  <div>Addres line dummy here<br>Addres line dummy here</div>
</div>

<div class="abs f-rule" style="top:5010px"></div>
<div class="abs f-links"><span>ABOUT US</span><span>SERVICES</span><span>ENQUIRIES</span><span>REVIEWS</span><span>CONTACT US</span></div>
<div class="abs f-rule" style="top:5098px"></div>
<div class="abs copyright">Copyright © 2026 All Rights Reserved By Varlow Landscaping</div>
<div class="abs socials"><span></span><span></span><span></span><span></span></div>

</body>
</html>
```